TALBRIN ELEVATOR CORP

LOOKING FOR BLACK MATTE BACKGROUND WITH GLOSS DESIGN
NEED RAISED UV ON LOGO AND LETTERING , WITH ROUNDED CORNERS AND COLORED EDGES ( FLOURECENT BLUE)

```html
<!DOCTYPE html>
<html lang="en">
<head>
<meta charset="utf-8">
<title>Talbrin Elevator Corp — Business Card</title>
<link href="https://fonts.googleapis.com/css2?family=Cinzel:wght@600&family=Roboto:wght@400;500&display=swap" rel="stylesheet">
<style>
  :root {
    --page-bg: #e4e4e4;
    --card-white: #ffffff;
    --card-black: #2b2b2b;
    --edge-blue: #2f7fe0;
    --brand-blue: #2f6fc4;
    --link-blue: #3a82d8;
    --ink: #2a2a2a;
    --ink-soft: #3c3c3c;
    --on-dark: #f4f4f4;
  }
  * { margin: 0; padding: 0; box-sizing: border-box; }
  html, body { width: 1200px; height: 801px; overflow: hidden; }
  body {
    background: var(--page-bg);
    position: relative;
    font-family: "Roboto", Arial, sans-serif;
  }
  .card {
    position: absolute;
    top: 246px;
    width: 540px;
    height: 309px;
    border-radius: 12px;
    overflow: hidden;
    border-bottom: 4px solid var(--edge-blue);
    border-left: 2px solid var(--edge-blue);
    box-shadow: 0 6px 18px rgba(0,0,0,0.18);
  }
  .card-front { left: 40px; background: var(--card-white); }
  .card-back  { left: 620px; background: var(--card-black); }

  /* front */
  .front-disc {
    position: absolute;
    left: 250px; top: -110px;
    width: 340px; height: 340px;
    border-radius: 50%;
    background: var(--brand-blue);
  }
  .front-brand {
    position: absolute;
    left: 28px; top: 34px;
    font-family: "Cinzel", "Times New Roman", serif;
    font-weight: 600;
    font-size: 15px;
    letter-spacing: 0.5px;
    color: var(--ink);
  }
  .front-tagline {
    position: absolute;
    left: 40px; top: 54px;
    font-family: "Cinzel", "Times New Roman", serif;
    font-weight: 600;
    font-size: 10px;
    color: var(--ink);
  }
  .person { position: absolute; left: 28px; top: 104px; }
  .person-name { font-size: 26px; font-weight: 500; color: var(--link-blue); line-height: 1.1; }
  .person-title { font-size: 17px; color: var(--ink-soft); }
  .address {
    position: absolute; left: 28px; top: 172px;
    font-size: 14px; line-height: 1.35; color: var(--ink-soft);
  }
  .contacts {
    position: absolute; left: 28px; top: 222px;
    list-style: none; font-size: 14px; line-height: 1.55; color: var(--ink-soft);
  }
  .contacts li { display: flex; align-items: center; gap: 8px; }
  .contacts svg { width: 12px; height: 12px; flex: none; }
  .contacts .accent { color: var(--link-blue); }

  /* back */
  .back-lockup {
    position: absolute; inset: 0;
    display: flex; flex-direction: column; align-items: center; justify-content: center;
    gap: 10px;
  }
  .back-disc { width: 86px; height: 86px; border-radius: 50%; background: var(--brand-blue); }
  .back-brand {
    font-family: "Cinzel", "Times New Roman", serif;
    font-weight: 600; font-size: 27px; letter-spacing: 0.5px;
    color: var(--on-dark);
  }
  .back-tagline {
    font-family: "Cinzel", "Times New Roman", serif;
    font-weight: 600; font-size: 17px;
    color: var(--on-dark); margin-top: -8px;
  }
</style>
</head>
<body>

<section class="card card-front" aria-label="Card front">
  <div class="front-disc"></div>
  <div class="front-brand">TALBRIN ELEVATOR CORP</div>
  <div class="front-tagline">ELEVATOR SERVICES</div>

  <div class="person">
    <div class="person-name">Martin Hale</div>
    <div class="person-title">President</div>
  </div>

  <address class="address" style="font-style:normal">
    2271 Orchard Park Avnue<br>
    Bronx, Ny 10460
  </address>

  <ul class="contacts">
    <li>
      <svg viewBox="0 0 12 12" aria-hidden="true"><path d="M2.5 1 L4.5 1 L5 3.5 L3.8 4.4 C4.5 6 6 7.5 7.6 8.2 L8.5 7 L11 7.5 L11 9.5 C11 10.3 10.3 11 9.5 11 C5 11 1 7 1 2.5 C1 1.7 1.7 1 2.5 1 Z" fill="var(--brand-blue)"/></svg>
      555-014-2736
    </li>
    <li>
      <svg viewBox="0 0 12 12" aria-hidden="true"><rect x="1" y="2.5" width="10" height="7" fill="none" stroke="var(--brand-blue)" stroke-width="1.2"/><path d="M1 2.5 L6 6.5 L11 2.5" fill="none" stroke="var(--brand-blue)" stroke-width="1.2"/></svg>
      talbrinelevator@mail.com
    </li>
    <li>
      <svg viewBox="0 0 12 12" aria-hidden="true"><circle cx="6" cy="6" r="5" fill="none" stroke="var(--brand-blue)" stroke-width="1.2"/><path d="M1 6 H11 M6 1 C3.5 3.5 3.5 8.5 6 11 M6 1 C8.5 3.5 8.5 8.5 6 11" fill="none" stroke="var(--brand-blue)" stroke-width="1"/></svg>
      <span>www.<span class="accent">talbrinelevatorny</span>.com</span>
    </li>
  </ul>
</section>

<section class="card card-back" aria-label="Card back">
  <div class="back-lockup">
    <div class="back-disc"></div>
    <div class="back-brand">TALBRIN ELEVATOR CORP</div>
    <div class="back-tagline">ELEVATOR SERVICES</div>
  </div>
</section>

</body>
</html>
```